TIDAL VERGE needs bisness cards pronto

Bisness name is "TIDAL VERGE" new bisness the bisness includes lawn mowing, garden matanace, and any jobs around the house.
I need a card that is colorful and vibrant and the bisness of lawn mowing maybe with some nature with it. It also needs my contact details"Darren Quellby mobile 0413562049 call for free quote and email norma.vance@fernmail.com.au and a catchy tag line

Industry/Entity Type

House

Requirements
Must have
• Bisness name "TIDAL VERGE"
Contact details "0413562049"
Email norma.vance@fernmail.com.au
Call for free quote

```html
<!DOCTYPE html>
<html lang="en">
<head>
<meta charset="utf-8">
<title>TIDAL VERGE – Business Card</title>
<link rel="stylesheet" href="https://fonts.googleapis.com/css2?family=Open+Sans:wght@700;800&display=swap">
<style>
  :root {
    --page: #ecebe6;
    --card-green: #1fa84a;
    --card-shadow: rgba(0, 0, 0, 0.18);
    --quote-green: #179040;
    --quote-edge: #0f7a33;
    --tag-orange: #f08a24;
    --tag-lime: #8cc63f;
    --tag-red: #e8262d;
    --tag-blue: #1e9ad6;
    --tag-yellow: #c8d82a;
    --white: #ffffff;
    --ink: #1d1d1d;
  }
  * { box-sizing: border-box; margin: 0; padding: 0; }
  html, body {
    width: 937px;
    height: 1200px;
    overflow: hidden;
    background: var(--page);
    font-family: "Open Sans", Arial, sans-serif;
  }
  .sheet {
    position: relative;
    width: 937px;
    height: 1200px;
  }
  .card {
    position: absolute;
    left: 88px;
    width: 760px;
    height: 435px;
    background: var(--card-green);
    box-shadow: 0 10px 28px var(--card-shadow);
    overflow: hidden;
  }
  .card--front { top: 110px; }
  .card--back { top: 655px; }

  .brand-name {
    color: var(--white);
    font-weight: 800;
    text-transform: uppercase;
    line-height: 0.88;
    letter-spacing: -1px;
  }
  .card--front .brand-name {
    position: absolute;
    left: 40px;
    top: 128px;
    font-size: 70px;
  }
  .card--back .brand-name {
    position: absolute;
    left: 0;
    right: 0;
    top: 50%;
    transform: translateY(-50%);
    text-align: center;
    font-size: 104px;
  }

  .tag {
    position: absolute;
    color: var(--white);
    font-weight: 700;
    font-size: 22px;
    line-height: 1.1;
    padding: 5px 16px;
    display: flex;
    align-items: center;
    gap: 12px;
    white-space: nowrap;
  }
  .tag--mowing { background: var(--tag-orange); left: 400px; top: 28px; width: 200px; }
  .tag--garden { background: var(--tag-lime); left: 350px; top: 68px; width: 230px; }
  .tag--jobs {
    background: var(--tag-red);
    left: 400px; top: 108px; width: 300px;
    white-space: normal;
    text-align: center;
    display: block;
  }
  .tag--phone { background: var(--tag-blue); left: 420px; top: 186px; width: 280px; font-size: 24px; }
  .tag--email { background: var(--tag-yellow); left: 232px; top: 292px; width: 490px; font-size: 21px; }
  .tag svg { flex: none; }

  .quote-box {
    position: absolute;
    left: 232px;
    top: 342px;
    width: 250px;
    height: 74px;
    background: var(--quote-green);
    border: 2px solid var(--quote-edge);
    color: var(--white);
    font-weight: 700;
    font-size: 20px;
    display: flex;
    align-items: center;
    padding-left: 18px;
  }
</style>
</head>
<body>
<main class="sheet">
  <section class="card card--front" aria-label="Business card front">
    <h1 class="brand-name">Tidal<br>Verge</h1>

    <p class="tag tag--mowing">lawn mowing</p>
    <p class="tag tag--garden">garden matanace</p>
    <p class="tag tag--jobs">any jobs around<br>the house</p>

    <p class="tag tag--phone">
      <svg width="30" height="24" viewBox="0 0 30 24" aria-hidden="true">
        <path d="M3 8 Q15 0 27 8 L25 12 L20 10 L19 7 Q15 5.5 11 7 L10 10 L5 12 Z" fill="var(--ink)"/>
        <path d="M9 12 H21 L25 22 H5 Z" fill="var(--ink)"/>
        <circle cx="15" cy="17" r="2.6" fill="var(--tag-blue)"/>
      </svg>
      0413562049
    </p>

    <p class="tag tag--email">
      <svg width="28" height="20" viewBox="0 0 28 20" aria-hidden="true">
        <rect x="1" y="1" width="26" height="18" fill="var(--ink)"/>
        <path d="M2 2 L14 11 L26 2" stroke="var(--tag-yellow)" stroke-width="2" fill="none"/>
      </svg>
      norma.vance@fernmail.com.au
    </p>

    <p class="quote-box">Call for free quote</p>
  </section>

  <section class="card card--back" aria-label="Business card back">
    <h2 class="brand-name">Tidal<br>Verge</h2>
  </section>
</main>
</body>
</html>
```